Mailer Box Design

Needed: Design for a folding mailer box that are used for sending golf gift items to (male) customers.
Colors: 1-2 print colors + option Box color can be used (white or kraft brown)

Outside: Company logo on top and bottom, website on two sides, two sides free for design ideas.

Inside: pattern for inside top lid and sides, bottom will have social media icons and 20-30 words of text.

*Pattern inside sample box image is not a pattern style suitable for this project.
*Text Fronts are Segoe

```html
<!DOCTYPE html>
<html lang="en">
<head>
<meta charset="utf-8">
<title>Fairway Crate – Mailer Box Dieline</title>
<link rel="stylesheet" href="https://fonts.googleapis.com/css2?family=Open+Sans:wght@400;700&display=swap">
<style>
  :root {
    --backdrop: #fdd277;
    --print-black: #000000;
    --kraft: #c4a373;
    --kraft-dark: #a98a5c;
    --shadow: rgba(60, 40, 0, 0.45);
  }
  html, body {
    margin: 0;
    padding: 0;
    width: 1200px;
    height: 1200px;
    overflow: hidden;
    background: var(--backdrop);
  }
  .sheet {
    display: block;
    width: 1200px;
    height: 1200px;
    font-family: "Open Sans", sans-serif;
  }
  .dieline { filter: drop-shadow(5px 5px 2px var(--shadow)); }
  .panel-black { fill: var(--print-black); }
  .panel-kraft { fill: url(#kraftPattern); }
  .ball-art { fill: url(#ballTone); stroke: var(--kraft); stroke-width: 5; }
  .wordmark { fill: var(--kraft); font-weight: 700; font-size: 40px; letter-spacing: 1px; }
  .website { fill: var(--kraft); font-weight: 700; font-size: 10px; }
  .info-card { fill: var(--kraft); stroke: var(--print-black); stroke-width: 2; }
  .info-title { fill: var(--print-black); font-weight: 700; font-size: 13px; }
  .social-dot { fill: var(--print-black); }
  .social-handle { fill: var(--print-black); font-size: 7px; }
  .info-body { fill: var(--print-black); font-size: 9.5px; }
</style>
</head>
<body>
<svg class="sheet" viewBox="0 0 1500 1500" xmlns="http://www.w3.org/2000/svg">
  <defs>
    <radialGradient id="ballTone" cx="40%" cy="55%" r="60%">
      <stop offset="0%" stop-color="#000"/>
      <stop offset="70%" stop-color="#2a2116"/>
      <stop offset="100%" stop-color="#6e5a3c"/>
    </radialGradient>
    <linearGradient id="kraftPattern" x1="0" y1="0" x2="1" y2="1">
      <stop offset="0%" stop-color="#b89767"/>
      <stop offset="50%" stop-color="#c4a373"/>
      <stop offset="100%" stop-color="#b08f60"/>
    </linearGradient>
    <clipPath id="outerFlapClip">
      <path d="M210,190 Q210,108 300,108 H582 Q672,108 672,190 Z"/>
    </clipPath>
    <clipPath id="outerBodyClip">
      <path d="M155,478 H728 V930 H155 Z"/>
    </clipPath>
  </defs>

  <!-- Outside print: black on kraft board -->
  <g class="dieline outside-face">
    <path class="panel-black tuck-flap" d="M210,190 Q210,108 300,108 H582 Q672,108 672,190 Z"/>
    <rect class="panel-black lid-panel" x="215" y="200" width="452" height="275" rx="30"/>
    <path class="panel-black body-panel" d="M155,478 H728 V555 L680,562 V565 H773 V848 H680 L728,855 V930 H155 V855 L203,848 H108 V565 H203 L155,558 Z"/>
    <rect class="panel-black side-tab" x="104" y="628" width="8" height="44"/>
    <rect class="panel-black side-tab" x="104" y="738" width="8" height="44"/>
    <rect class="panel-black side-tab" x="770" y="628" width="8" height="44"/>
    <rect class="panel-black side-tab" x="770" y="738" width="8" height="44"/>

    <g clip-path="url(#outerFlapClip)">
      <circle class="ball-art" cx="440" cy="108" r="85" role="img" aria-label="Golf ball illustration with dimples"/>
    </g>

    <text class="website" x="440" y="235" text-anchor="middle" transform="rotate(180 440 231)">www.fairwaycrategolf.com</text>
    <text class="wordmark" x="440" y="334" text-anchor="middle" transform="rotate(180 440 320)">FAIRWAY CRATE</text>

    <circle class="ball-art" cx="440" cy="500" r="108" role="img" aria-label="Golf ball illustration with dimples"/>

    <text class="wordmark" x="440" y="702" text-anchor="middle">FAIRWAY CRATE</text>
    <text class="website" x="440" y="775" text-anchor="middle">www.fairwaycrategolf.com</text>

    <g clip-path="url(#outerBodyClip)">
      <circle class="ball-art" cx="440" cy="918" r="108" role="img" aria-label="Golf ball illustration with dimples"/>
    </g>
  </g>

  <!-- Inside print: pattern on kraft board -->
  <g class="dieline inside-face" role="img" aria-label="Repeating pattern of golf balls with golfer silhouettes">
    <path class="panel-kraft tuck-flap" d="M830,612 Q830,530 920,530 H1200 Q1290,530 1290,612 Z"/>
    <rect class="panel-kraft lid-panel" x="835" y="620" width="452" height="275" rx="30"/>
    <path class="panel-kraft body-panel" d="M773,898 H1347 V975 L1299,982 V985 H1392 V1268 H1299 L1347,1275 V1353 H773 V1275 L821,1268 H727 V985 H821 L773,978 Z"/>
  </g>

  <g class="social-card">
    <rect class="info-card" x="938" y="1017" width="242" height="160" rx="8"/>
    <text class="info-title" x="1059" y="1042" text-anchor="middle">Share Your Experience with Us</text>
    <circle class="social-dot" cx="1000" cy="1078" r="22"/>
    <circle class="social-dot" cx="1054" cy="1078" r="22"/>
    <circle class="social-dot" cx="1108" cy="1078" r="22"/>
    <text class="social-handle" x="1000" y="1113" text-anchor="middle">fairwaycrate</text>
    <text class="social-handle" x="1054" y="1113" text-anchor="middle">@FairwayCrate_Golf</text>
    <text class="social-handle" x="1108" y="1113" text-anchor="middle">fairwaycrate</text>
    <text class="info-body" x="1059" y="1131" text-anchor="middle">Lorem ipsum dolor sit amet, consectetur adipis</text>
    <text class="info-body" x="1059" y="1142" text-anchor="middle">cing elit, sed do eiusmod tempor incididunt ut</text>
    <text class="info-body" x="1059" y="1153" text-anchor="middle">labore et dolore magna aliqua. Ut enim ad minim</text>
  </g>
</svg>
</body>
</html>
```